Modern home page design for insurance and investment business

- The design should be based around the attached HPID (home page information design) called KTW HPID. The table boxes are just for approximate placement of information – you DON'T have to make it look exactly like this.
- Information only is in orange text. Copy to go on the design in black text. Some instructions are in the HPID. Please be creative! You don’t have to use the exact images provided if you have a better idea.

- The design needs to be clean and spacious. Please use the colours from the logos in the website design. Lots of white too.

I've attached home page gallery example photos. You can use any of these photos or something similar with the words from one of the photos.

- Expected standard of design examples: (Please DO NOT copy these exactly – they are just examples)
http://www.harbourvane.co.nz/
https://www.brightkeel.co.nz/
http://sandorelcover.co.nz/homepage/

Width of content will be 1100 pixels when implemented as a web page. Header height (without nav bar) 150-160 pixels.

The winning PSD file will have to be provided as follows…
1. Canvas size of 2000px x 2000px - 72ppi in Adobe Photoshop (CS5 compatible)
2. Width of content section is 1100px wide - centered in the canvas
3. Any button rollovers/hovers in the PSD as hidden layers.
4. All fonts used must be Google fonts (except for the fonts in the header at the top of the page).
5. You will need to supply the chosen home page plus one example page (example page as a style guide for how all other pages will look). Example page is only the header and navigational bar at the top, an empty sector in the middle with a column (180 px wide) which can be left or right aligned which means the main sector is 920 pixels wide, and then the footer at the bottom of the page.

```html
<!DOCTYPE html>
<html lang="en">
<head>
<meta charset="utf-8">
<title>KTW Insure &amp; Invest</title>
<link rel="stylesheet" href="https://fonts.googleapis.com/css2?family=Questrial&family=Lato:wght@400;700&display=swap">
<style>
:root{
  --navy:#0c4a80;
  --blue:#16568f;
  --text:#333;
  --muted:#777;
  --line:#dcdcdc;
  --footer:#e7e7e7;
  --white:#fff;
}
*{box-sizing:border-box;margin:0;padding:0}
html,body{width:803px;height:1200px;overflow:hidden;background:var(--white)}
body{position:relative;font-family:"Questrial",sans-serif;color:var(--text)}
.abs{position:absolute;white-space:nowrap}

.site-header{position:absolute;left:0;top:0;width:803px;height:104px;background:linear-gradient(#fff,#ececec)}
.brand{left:129px;top:26px;display:flex;align-items:center;gap:8px}
.brand-name{font-size:34px;color:var(--navy);letter-spacing:1px;line-height:1}
.brand-dot{width:22px;height:22px;border-radius:50%;background:var(--navy)}
.region-map{left:268px;top:14px;width:52px;height:52px;border-radius:50%;background:radial-gradient(#eeeae0,#d5cfbe);border:1px solid #ccc}
.region-text{left:327px;top:30px;font-size:8px;line-height:12px;color:var(--muted)}
.header-info{right:129px;top:20px;text-align:right;color:var(--muted)}
.header-info .tag{font-size:8px}
.header-info .links{font-size:9px;margin-top:3px}
.header-info .phone{font-size:12.5px;color:var(--navy);margin-top:2px}

.main-nav{left:129px;top:80px;width:545px;height:24px;background:var(--white);font-size:9px}
.main-nav a{position:absolute;top:0;height:24px;color:#222;text-decoration:none;line-height:24px;white-space:nowrap}
.main-nav a.active{background:var(--navy);color:#fff;text-align:center}

.hero{left:0;top:104px;width:803px;height:271px;background:linear-gradient(100deg,#b9b9b4 0%,#cfcfcb 35%,#a8ad8e 55%,#d9dcda 75%,#e3e5e6 100%)}
.hero-title{left:445px;top:212px;font-size:19px;color:#111}

.card{top:341px;width:272px;height:179px;background:linear-gradient(#fff,#ececec);text-align:center;padding:16px 14px 0;box-shadow:0 1px 2px rgba(0,0,0,.15);white-space:normal}
.card h2{font-weight:400;font-size:15px;color:var(--blue)}
.card p{font-size:7.2px;line-height:14px;color:#666;margin-top:9px}
.card-icon{display:block;margin:6px auto 0}
.btn-ghost{display:inline-block;margin-top:1px;border:1px solid #ccc;background:#fff;font-family:"Lato",sans-serif;font-size:7.5px;color:#444;padding:4px 8px}

.section-title{left:129px;top:550px;width:545px;text-align:center;font-size:15px;font-weight:400;color:var(--blue)}
.section-title span{background:#fff;padding:0 10px;position:relative}
.section-title::before{content:"";position:absolute;left:0;right:0;top:10px;border-top:1px solid var(--line)}
.stage-photo{top:604px;width:131px;height:98px}

.callback{left:129px;top:730px;width:545px;height:180px;border:1px solid #ececec}
.callback h2{position:absolute;left:0;right:0;top:15px;text-align:center;font-weight:400;font-size:15px;color:var(--blue)}
.field{top:781px;height:20px;border:1px solid #d6d6d6;background:#fff;font-size:7.5px;color:#555;padding:5px 6px}
.message{left:184px;top:808px;width:434px;height:58px}
.btn-send{left:368px;top:875px;width:67px;height:23px;background:var(--navy);color:#fff;font-family:"Lato",sans-serif;font-size:7.5px;text-align:center;line-height:23px;border-radius:2px}

.site-footer{left:0;top:937px;width:803px;height:231px;background:var(--footer);border-top:2px solid #d0d0d0}
.f-main{font-size:9.5px;color:#222;line-height:12px}
.f-head{font-size:8px;color:#222;line-height:10px}
.f-sub{font-size:7px;color:#777;line-height:10px}
.contact-head{left:129px;top:1094px;width:545px;text-align:center;font-size:9.5px;color:#222}
.contact-head::before{content:"";position:absolute;left:0;right:0;top:14px;border-top:1px solid #d2d2d2}
.contact-item{top:1120px;display:flex;gap:12px;align-items:flex-start;font-size:7.5px;line-height:12px;color:#444}
.copyright{left:0;top:1180px;width:803px;text-align:center;font-size:7px;color:#444}
</style>
</head>
<body>

<header class="site-header">
  <div class="abs brand"><span class="brand-name">KTW</span><span class="brand-dot"></span></div>
  <div class="abs region-map" role="img" aria-label="Small round map of the Kowhai Bay region"></div>
  <div class="abs region-text">Servicing Clients New Zealand Wide<br>Located in Sunny Kowhai Bay</div>
  <div class="abs header-info">
    <div class="tag">Smart financial decisions for today and for your future</div>
    <div class="links">Insurances &nbsp;|&nbsp; Investments &nbsp;|&nbsp; Financial Planning</div>
    <div class="phone">0800 555 0142, 06 555 0142</div>
  </div>
</header>

<nav class="abs main-nav">
  <a class="active" style="left:0;width:39px">Home</a>
  <a style="left:46px">About</a>
  <a style="left:84px">What We Do</a>
  <a style="left:148px">What Life Stage are You?</a>
  <a style="left:263px">Insurances</a>
  <a style="left:321px">Investments</a>
  <a style="left:384px">FAQs</a>
  <a style="left:418px">Consultation</a>
  <a style="left:481px">Contact/Map</a>
</nav>

<div class="abs hero" role="img" aria-label="Photo of a person with a blue umbrella standing on a misty gravel road beside a lake"></div>
<div class="abs hero-title">Planning for a rainy day...</div>

<section class="abs card" style="left:130px">
  <h2>Insurance</h2>
  <p>An overview of insurance from the point of view of benefits to the customer of working with KTW will be in this space..... Relevant keywords such as the types of insurances e.g. life insurance, travel insurance etc will be mentioned... Should be inviting to both new and current customers....</p>
  <svg class="card-icon" width="22" height="32" viewBox="0 0 22 32" aria-hidden="true"><path d="M3 9 Q11 -1 19 9 Z" fill="#111"/><line x1="11" y1="6" x2="11" y2="14" stroke="#111"/><circle cx="8" cy="14" r="2" fill="#111"/><rect x="6" y="17" width="4" height="14" fill="#111"/></svg>
  <span class="btn-ghost">Find out more</span>
</section>
<section class="abs card" style="left:403px">
  <h2>Investment</h2>
  <p>An overview of insurance from the point of view of benefits to the customer of working with KTW will be in this space..... Relevant keywords such as the types of insurances e.g. life insurance, travel insurance etc will be mentioned... Should be inviting to both new and current customers....</p>
  <svg class="card-icon" width="22" height="32" viewBox="0 0 22 32" aria-hidden="true"><rect x="2" y="22" width="5" height="9" fill="#111"/><rect x="8.5" y="16" width="5" height="15" fill="#111"/><rect x="15" y="9" width="5" height="22" fill="#111"/><path d="M3 16 L10 8 L15 3" stroke="#111" fill="none"/></svg>
  <span class="btn-ghost">Find out more</span>
</section>

<h2 class="abs section-title"><span>What life stage are you at?</span></h2>
<div class="abs stage-photo" style="left:129px;background:linear-gradient(135deg,#f1ece6,#d9c2a6)" role="img" aria-label="Young couple with speech bubbles asking about starting financial planning and insurance"></div>
<div class="abs stage-photo" style="left:267px;background:linear-gradient(135deg,#cfe0f0,#9fb27a)" role="img" aria-label="Family outdoors with speech bubbles asking about investments and insurance cover"></div>
<div class="abs stage-photo" style="left:405px;background:linear-gradient(135deg,#7fb0e0,#2f6fb0)" role="img" aria-label="Middle-aged couple by the sea with speech bubbles asking about retirement savings"></div>
<div class="abs stage-photo" style="left:543px;background:linear-gradient(135deg,#f3efe4,#c9b98a)" role="img" aria-label="Retired couple with speech bubbles asking about holidays, wills and downsizing"></div>

<section class="abs callback"><h2>Would you like KTW to call you? Fill in the form and we’ll be in touch</h2></section>
<div class="abs field" style="left:184px;width:103px">First name</div>
<div class="abs field" style="left:295px;width:103px">Last name</div>
<div class="abs field" style="left:405px;width:103px">Email</div>
<div class="abs field" style="left:516px;width:103px">Contact phone</div>
<div class="abs field message">Message</div>
<div class="abs btn-send">SEND</div>

<footer class="abs site-footer"></footer>

<div class="abs f-main" style="left:129px;top:957px">Home</div>
<div class="abs f-main" style="left:129px;top:975px">About</div>
<div class="abs f-sub" style="left:129px;top:996px">Meet the Team</div>
<div class="abs f-sub" style="left:129px;top:1011px">Testimonials</div>
<div class="abs f-main" style="left:129px;top:1032px">What We Do</div>
<div class="abs f-main" style="left:129px;top:1050px">FAQs</div>
<div class="abs f-main" style="left:129px;top:1067px">Consultation</div>

<div class="abs f-main" style="left:256px;top:957px">What Life Stage are You?</div>
<div class="abs f-sub" style="left:256px;top:975px">Life stage 18-30 years</div>
<div class="abs f-sub" style="left:256px;top:993px">Life stage 30-45 years</div>
<div class="abs f-sub" style="left:256px;top:1010px">Life stage 45-65 years</div>
<div class="abs f-sub" style="left:256px;top:1028px">Life stage 65+ years</div>

<div class="abs f-main" style="left:433px;top:957px">Products/Services</div>
<div class="abs f-head" style="left:433px;top:975px">Insurance</div>
<div class="abs f-sub" style="left:433px;top:991px">Life insurance</div>
<div class="abs f-sub" style="left:433px;top:1008px">Trauma insurance</div>
<div class="abs f-sub" style="left:433px;top:1026px">Disablement cover</div>
<div class="abs f-sub" style="left:433px;top:1044px">Income protection</div>
<div class="abs f-sub" style="left:520px;top:991px">Health insurance</div>
<div class="abs f-sub" style="left:520px;top:1008px">Business insurance</div>
<div class="abs f-sub" style="left:520px;top:1026px">Fire &amp; General</div>
<div class="abs f-sub" style="left:520px;top:1044px">Travel insurance</div>
<div class="abs f-head" style="left:606px;top:977px">Investment</div>
<div class="abs f-sub" style="left:606px;top:991px">Retirement Saver</div>

<div class="abs contact-head"><span style="background:var(--footer);padding:0 8px;position:relative">Contact/Map</span></div>
<div class="abs contact-item" style="left:135px">
  <svg width="14" height="22" viewBox="0 0 14 22" aria-hidden="true"><path d="M7 0 C2 0 0 4 0 7 C0 12 7 22 7 22 C7 22 14 12 14 7 C14 4 12 0 7 0 Z" fill="#999"/><circle cx="7" cy="7" r="2.5" fill="#e7e7e7"/></svg>
  <div>48 Harbour Row, Kowhai Bay<br>New Zealand, PO Box 4417, Kowhai Bay</div>
</div>
<div class="abs contact-item" style="left:323px">
  <svg width="26" height="24" viewBox="0 0 26 24" aria-hidden="true"><path d="M2 1 H24 L14 12 L24 23 H2 L12 12 Z" fill="none" stroke="#999" stroke-width="2"/><path d="M6 21 L13 14 L20 21 Z" fill="#999"/></svg>
  <div style="margin-top:6px">Office Hours: 8.30 – 5.00 PM</div>
</div>
<div class="abs contact-item" style="left:489px">
  <svg width="24" height="24" viewBox="0 0 24 24" aria-hidden="true"><path d="M5 1 L9 6 L7 9 C8 12 11 15 14 16 L17 14 L22 18 L19 22 C10 22 2 13 2 4 Z" fill="#999"/></svg>
  <div>After Hours Please phone:<br>0800 555 0142, 06 555 0142</div>
</div>

<div class="abs copyright">© Copyright 2014 KTW Insure &amp; Invest. All rights reserved.</div>

</body>
</html>
```